This book will apply the 12 Steps to gaming addiction, also known as video game addiction. The primary purpose of the book is to provide an effective solution for this new type of addiction. The solution is based on the rich and successful concepts of traditional twelve-step programs like RL.

The title on the cover will be "Nine Doors Past the Glowing Screen" and "by Martin Quorby". A subtitle can be used if it works in your design of "A Practical Path Beyond Compulsive Console Play". Cover will be for a 6" x 9" book approximately 110 pages in length.

Some back cover text including some review quotes and an author bio are in the attached Word doc. There is also an author photo attached for for the back cover.

Requirements
Must have
• For the cover design it could be stylized, or an image, a partial image, or whatever. I am open to suggestions. Think about what would be noticed by a person searching for help with moderating their video game use, or by the parents or loved ones of problem gamers. Something contemporary and eye catching.

```html
<!DOCTYPE html>
<html lang="en">
<head>
<meta charset="utf-8">
<title>Nine Doors Past the Glowing Screen – Book Cover</title>
<link rel="stylesheet" href="https://fonts.googleapis.com/css2?family=Oswald:wght@500;600&family=Noto+Serif:ital,wght@0,400;0,700;1,400&family=Merriweather:wght@700&display=swap">
<style>
  :root {
    --navy: #2b2f5f;
    --band: #2e3265;
    --red: #8f1d24;
    --quote-red: #9a1f22;
    --ink: #2a2d55;
    --yellow: #f2e48c;
    --lavender: #c3c6dd;
    --slot: #f4f4f6;
  }
  * { margin: 0; padding: 0; box-sizing: border-box; }
  html, body { width: 1200px; height: 882px; overflow: hidden; }
  body { background: #fff; }

  .cover-spread {
    position: relative; width: 1200px; height: 882px; overflow: hidden;
    background:
      radial-gradient(ellipse 420px 330px at 900px 260px, #ffffff 0%, rgba(255,255,255,0) 100%),
      linear-gradient(90deg, var(--lavender) 0%, #e6e7f1 38%, #eef0f6 52%, #dfe1ee 100%);
    font-family: "Noto Serif", Georgia, serif;
    color: var(--ink);
  }

  .bottom-band {
    position: absolute; left: 0; right: 0; top: 792px; height: 90px;
    background: var(--band);
  }

  /* Back cover */
  .back-title {
    position: absolute; left: 35px; top: 42px; width: 527px;
    font-family: "Oswald", "Arial Narrow", sans-serif; font-weight: 500;
    font-size: 29px; line-height: 1.2; letter-spacing: 1.2px; color: var(--navy); white-space: nowrap;
  }
  .reviews { position: absolute; left: 38px; top: 86px; width: 522px; }
  .review { font-size: 12px; line-height: 14.6px; margin-bottom: 14.6px; }
  .review-source { color: var(--quote-red); }
  .review-source em { font-style: italic; }
  .back-rule {
    position: absolute; left: 32px; top: 347px; width: 529px; height: 2px;
    background: var(--navy);
  }
  .blurb { position: absolute; left: 38px; top: 364px; width: 522px; }
  .blurb p { font-size: 12px; line-height: 14.6px; margin-bottom: 14.6px; }

  .author-photo {
    position: absolute; left: 32px; top: 626px; width: 254px; height: 231px;
    background:
      radial-gradient(ellipse 70px 90px at 128px 100px, #c99a80 0%, rgba(201,154,128,0) 100%),
      linear-gradient(180deg, #7b8a4e 0%, #a3865c 45%, #2b2c3a 100%);
  }
  .author-bio {
    position: absolute; left: 304px; top: 622px; width: 250px;
    font-style: italic; font-size: 10.4px; line-height: 13px; color: var(--ink);
  }
  .isbn-slot {
    position: absolute; left: 367px; top: 740px; width: 195px; height: 117px;
    background: var(--slot);
  }

  /* Spine */
  .spine-title, .spine-author {
    position: absolute; left: 589px; writing-mode: vertical-rl;
    font-family: "Oswald", "Arial Narrow", sans-serif; font-weight: 500;
    font-size: 14px; letter-spacing: 1px; white-space: nowrap;
  }
  .spine-title { top: 46px; color: var(--navy); }
  .spine-author {
    top: 732px;
    background: linear-gradient(180deg, var(--navy) 0, var(--navy) 60px, #ffffff 60px, #ffffff 100%);
    -webkit-background-clip: text; background-clip: text;
    color: transparent;
  }

  /* Front cover */
  .front-photo {
    position: absolute; left: 612px; top: 270px; width: 588px; height: 522px;
    background:
      radial-gradient(ellipse 150px 180px at 390px 150px, #d9b49c 0%, rgba(217,180,156,0) 100%),
      radial-gradient(ellipse 300px 220px at 380px 470px, #3a4560 0%, rgba(58,69,96,0) 100%),
      linear-gradient(180deg, rgba(238,239,246,0) 0%, rgba(200,204,222,0.5) 100%);
  }
  .front-kicker {
    position: absolute; left: 656px; top: 44px; width: 496px;
    display: flex; align-items: center; gap: 28px;
  }
  .front-kicker .rule { flex: 1; height: 2px; background: var(--navy); }
  .front-kicker span {
    font-family: "Oswald", "Arial Narrow", sans-serif; font-weight: 600;
    font-size: 46px; line-height: 1; color: var(--navy); letter-spacing: 1px;
  }
  .front-title-main {
    position: absolute; left: 644px; top: 106px; width: 528px; text-align: center;
    font-family: "Oswald", "Arial Narrow", sans-serif; font-weight: 600;
    font-size: 102px; line-height: 1; color: var(--navy); letter-spacing: 1px; white-space: nowrap;
  }
  .front-title-accent {
    position: absolute; left: 644px; top: 216px; width: 528px; text-align: center;
    font-family: "Oswald", "Arial Narrow", sans-serif; font-weight: 600;
    font-size: 58px; line-height: 1.1; color: var(--red); letter-spacing: 0.5px; white-space: nowrap;
  }
  .front-subtitle {
    position: absolute; left: 620px; top: 290px; width: 572px; text-align: center;
    font-size: 20px; color: var(--navy); white-space: nowrap;
  }
  .front-byline {
    position: absolute; left: 612px; top: 800px; width: 588px; text-align: center;
    font-family: "Merriweather", Georgia, serif; font-weight: 700;
    font-size: 42px; color: var(--yellow);
  }
</style>
</head>
<body>
<main class="cover-spread">
  <div class="bottom-band"></div>

  <!-- Back cover -->
  <h2 class="back-title">NINE DOORS PAST THE GLOWING SCREEN</h2>

  <section class="reviews">
    <p class="review">“A must-read for anyone who is addicted to or thinks they may have a problem with digital gaming. This eloquent work will also be useful to academics and clinicians exploring potential solutions. The author recognizes the similarities between gaming addiction and other addictions, and logically applies one of the most effective known solutions for addiction - The Twelve Steps.”<br>
      <span class="review-source">-- Dale Whitcombe, <em>Noted Interventionist and Keynote Speaker.</em></span></p>
    <p class="review">“If you suffer from digital gaming addiction, I strongly encourage you to use this book as your road map to get you back to the real world.”<br>
      <span class="review-source">-- Victor Ansel, <em>Founder of Network Growth Digest.</em></span></p>
    <p class="review">“As a high school teacher for 24 years, husband, father, coach, and 12-Step member, I can assure you that this book will transform the life of anyone who is addicted to video games. Well written, easy to understand, and a wonderful book that will provide you with a clear road map to recovery, and this includes teenagers, a group I have been working with in the classroom for decades.”<br>
      <span class="review-source">-- Paul Renner, <em>Lindale, OR High School Teacher.</em></span></p>
  </section>

  <div class="back-rule"></div>

  <section class="blurb">
    <p>An effective solution to the challenge of Digital Gaming Addiction (aka Video Game Addiction) based on the rich and successful tradition of the Twelve Steps.</p>
    <p>Addiction to Digital Gaming is a new and troubling phenomenon that has burst upon an unprepared society with alarming speed. Many people crave the use of Digital Games in a strikingly similar way to any other addict. Digital Games are a complex software and hardware system that have been designed to promote continued and progressive usage. This sophisticated technology clearly feeds on natural addictive tendencies.</p>
    <p>The 12 Steps are one of the most effective methods for treating addiction in human history. Originating with Recovery League in 1939, the 12 Steps have since been used to treat a variety of other addictions, including drugs, sex, gambling, eating disorders, and many others. Now in this groundbreaking work the 12 Steps are applied to the complex and evolving contemporary phenomenon of Digital Gaming Addiction.</p>
  </section>

  <div class="author-photo" role="img" aria-label="Author portrait: smiling man in a dark jacket before a leafy garden background"></div>
  <p class="author-bio">Martin Quorby is a Technology Consultant and Writer with many years of professional coding and consulting experience. He also struggled with addiction to drugs and alcohol and is now clean and sober in a Twelve-Step program for over 17 years. This unique combination of 12-Step experience and technology expertise led him to create Nine Doors Past the Glowing Screen.</p>
  <div class="isbn-slot"></div>

  <!-- Spine -->
  <div class="spine-title">NINE DOORS PAST THE GLOWING SCREEN</div>
  <div class="spine-author">BY MARTIN QUORBY</div>

  <!-- Front cover -->
  <div class="front-photo" role="img" aria-label="Photo of an intense young man gripping a game controller, his wrists cuffed to it"></div>
  <div class="front-kicker"><span class="rule"></span><span>NINE</span><span class="rule"></span></div>
  <h1 class="front-title-main">DOORS PAST</h1>
  <div class="front-title-accent">THE GLOWING SCREEN</div>
  <p class="front-subtitle">A Practical Path Beyond Compulsive Console Play</p>
  <p class="front-byline">by Martin Quorby</p>
</main>
</body>
</html>
```